Norwegian psychologist service needs a fresh and exiting web site*

Norwegian psychologist service: working with therapy, personal development, mastery and personal growth. Focus: children and teenagers with special needs; family dynamics; group processes; individuals with a need for therapy and personal growth. (Our company name: Fjordlys og samhold (means Mastery and Growth).

We already have a logo for the company, which will be used (will be attached in the project).

The webside is to be structured in 4 pages with roll down curtain menus (the numbers are just for guiding the designer - the should not be added):

Page 1: Om Fjordlys og Samhold (about Mastery and Growth): this is where our business is is presented/described shortly: Lorem Ipsum dolor cit...

Page 2: Tjenester (Services): this is where our 5 service areas are presented:
2.1 Utredning (Investigation, diagnosing): Lorem Ipsum dolor cit...
2.2 Rådgivning (consulting): Lorem Ipsum dolor cit...

2.3 Kurs og work shops (courses and work shops): Lorem Ipsum dolor cit...
2.3a Fjordlys og samhold Tema 1 (T1)
2.3b Fjordlys og samhold Tema 2 (T2)
2.3c Fjordlys og samhold Tema 3 (T3)

2.4 Terapi og utvikling (Therapy and development)
2.4a Fjordlys og samhold for individer (FS1)
2.4b Fjordlys og samhold i familier (FS2)
2.4c Fjordlys og samhold i grupper (FS3)
2.4d Fjordlys og samhold i institusjoner (FS4)

Page 3: Aktuelt (Blog): this is our blog where we share knowledge and articles

Page 4: Kontakt (Contact): This is the contact form page. Contact form should constitute:
- Ditt navn (your name)
- E-post (your e-mail)
- Emne (subject)
- Melding (message/description)

Our project should also include suggestion for handheld units (iPhone, iPad).
Updates

We have both been traveling with work for a while, and then unfortunately both of us got sick on return, so we need a few more days to evaluate and choose design. Kind Regards Arvid & Margit

Target Market(s)

Focus on therapy, learning, mastery and growth for children and teenagers with special needs, within the family dynamics, or in a group setting.
OUR MARKETS:
Private market: individuals, families, groups and health industry institutions (with focus on learning, mastery, growth (as well as growing up) and psychiatry for children and teenagers with special difficulties and needs)
Public institutions: Government institutions, state institutions and municipality institutions (e.g. schools, municipality health service, hospitals) that serve the public (families with children and teenagers with special needs, and where learning, mastery, growth (as well as growing up) and potential psychiatry is an issue).

Number of Pages Required

4 page

Font styles to use
Sans Serif

Colors

Designer to choose colors to be used in the design.

Requirements
Must have
• The website must have 4 pages with roll down curtain menus (we have added a PDF with suggested structure, and headings, with sub menus - see attached PDF drawing.
• The web page must also use the added logo file - and make the web page work well with our logo.
• We would like the website to have a modern look and we would like the site to be associated with typical HIGH END TOP QUALITY private health institutions, but with a stronger focus on human beings (hands, faces etc), and not white coats and doctors. We are psychologists in the private market.
• For instance, if photos are being used - we tend to like "warm" almost art-like, "grainy" two-tone (e.g. sepia) photos to illustrate our focus. If designer can find such photos as part of design, it would be interesting to us. We would like a few photos like that integrated in the design.
• We also want a design suggestion for how the web page should look like and behave on handheld units (e.g. iPhone, iPad).
Nice to have
• If designer could find a number of suitable photos that matches the business idea and design requirements (see description above), that could follow website, that would be good.
• It could also be nice to have graphic symbols that denote the different pages/subpages (subjects)....
• HORSES: we sometimes use horses as a "tool" in therapy sessions. The horse is not necessarily used for riding, but for contact, communication and grooming. PHOTOS: we would like the designer to find an opportunity for using a photo reflecting this cooperation between therapist, child, teenager and horse. It is a bit up to the designer to find a way to do this... Since the horse is only a tool, among many other tools, it does not have to be much - but we want to try and see how it will work with a photo that also reflects this part of our business.

```html
<!DOCTYPE html>
<html lang="no">
<head>
<meta charset="utf-8">
<title>Fjordlys og samhold – Tjenester</title>
<link rel="stylesheet" href="https://fonts.googleapis.com/css2?family=Lato:wght@300;400&family=Ubuntu:wght@400&family=Roboto+Condensed:wght@400&display=swap">
<style>
  :root {
    --purple: #8a1fd1;
    --purple-dark: #8419cf;
    --gold: #c8901c;
    --navy: #24357a;
    --text-grey: #7a7a7a;
    --white: #ffffff;
  }
  * { box-sizing: border-box; margin: 0; padding: 0; }
  html, body {
    width: 1200px; height: 2402px; overflow: hidden;
    background: var(--white);
    font-family: "Lato", sans-serif;
  }
  .page { position: relative; width: 1200px; height: 2402px; overflow: hidden; }

  .site-header {
    position: absolute; top: 0; left: 0; width: 1200px; height: 140px;
    background: var(--white);
  }
  .brand {
    position: absolute; left: 92px; top: 34px;
    display: flex; align-items: center; gap: 12px;
    color: var(--navy); font-family: "Lato", sans-serif; font-weight: 400;
  }
  .brand-mark { width: 22px; height: 22px; border-radius: 50%; background: var(--navy); }
  .brand-name { font-size: 26px; line-height: 30px; letter-spacing: 1px; text-transform: uppercase; width: 170px; }
  .menu-toggle {
    position: absolute; right: 92px; top: 34px; width: 84px; height: 84px;
    border-radius: 12px; background: var(--purple);
  }

  .hero {
    position: absolute; top: 140px; left: 0; width: 1200px; height: 190px;
    background: linear-gradient(90deg, #c8b8a6 0%, #d9c9b4 30%, #b8b0a6 55%, #8f8f98 80%, #84848e 100%);
  }

  .service { position: absolute; left: 72px; width: 1056px; height: 415px; }
  .service-photo { position: absolute; left: 0; top: 0; width: 415px; height: 415px; }
  .service-body { position: absolute; left: 460px; top: 8px; width: 545px; }
  .service-title {
    font-family: "Ubuntu", sans-serif; font-weight: 400;
    font-size: 54px; line-height: 62px; color: var(--purple);
  }
  .service-text {
    margin-top: 6px; font-weight: 300; font-size: 21px; line-height: 25px;
    color: var(--text-grey);
  }
  .more-button {
    display: block; margin-top: 36px; width: 272px; height: 50px;
    background: var(--gold); color: var(--white); text-align: center;
    font-family: "Roboto Condensed", sans-serif; font-size: 23px; line-height: 50px;
    text-decoration: none;
  }

  .photo-clinic { background: linear-gradient(135deg, #b9603a 0%, #d6c9b8 45%, #eae6de 100%); }
  .photo-family { background: linear-gradient(135deg, #6d7b9c 0%, #5b3c2c 40%, #2f8fc9 65%, #a9c83a 100%); }
  .photo-bulb { background: radial-gradient(circle at 45% 40%, #e2a763 0%, #6b5a4e 45%, #2a3338 100%); }
  .photo-sky { background: linear-gradient(180deg, #9fb0c5 0%, #b8c4d2 60%, #d3dbe4 100%); }

  .site-footer {
    position: absolute; left: 0; top: 2300px; width: 1200px; height: 102px;
    background: var(--purple-dark); color: var(--white); text-align: center;
  }
  .copyright { padding-top: 22px; font-family: "Roboto Condensed", sans-serif; font-size: 15px; }
  .social { margin-top: 14px; display: flex; justify-content: center; gap: 30px; }
  .social-dot { width: 22px; height: 22px; border: 2px solid var(--white); border-radius: 50%; }
</style>
</head>
<body>
<div class="page">
  <header class="site-header">
    <div class="brand">
      <span class="brand-mark"></span>
      <span class="brand-name">Fjordlys og samhold</span>
    </div>
    <svg class="menu-toggle" viewBox="0 0 84 84" aria-label="Meny">
      <rect width="84" height="84" rx="12" fill="#8a1fd1"/>
      <g stroke="#ffffff" stroke-width="3" stroke-linecap="round">
        <line x1="20" y1="31" x2="64" y2="31"/>
        <line x1="20" y1="42" x2="64" y2="42"/>
        <line x1="20" y1="53" x2="64" y2="53"/>
      </g>
    </svg>
  </header>

  <div class="hero" role="img" aria-label="Et barn som holder en voksen i hånden på en gate"></div>

  <main>
    <section class="service" style="top:390px">
      <div class="service-photo photo-clinic" role="img" aria-label="En behandler leser et ark ved en datamaskin"></div>
      <div class="service-body">
        <h2 class="service-title">Utredning</h2>
        <p class="service-text">Lorem ipsum dolor sit amet, consectetur adipiscing elit. Nunc auctor, lectus in ultrices semper, sapien mi venenatis mauris, id consectetur tortor dolor in mauris. Nunc porttitor massa vel sagittis lobortis. Aenean molestie lacinia mauris non bibendum. Nullam in mi eleifend, suscipit lorem ut, luctus sapien. Mauris id sapien eu ante vestibulum viverra. Cras auctor mi at nulla dictum mollis. Quisque faucibus sem magna, ut finibus orci fringilla id. Aliquam at augue eget eros euismod viverra non non quam.</p>
        <a class="more-button" href="#">vite mer</a>
      </div>
    </section>

    <section class="service" style="top:875px">
      <div class="service-photo photo-family" role="img" aria-label="En familie leser sammen med en rådgiver"></div>
      <div class="service-body">
        <h2 class="service-title">Rådgivning</h2>
        <p class="service-text">Lorem ipsum dolor sit amet, consectetur adipiscing elit. Nunc auctor, lectus in ultrices semper, sapien mi venenatis mauris, id consectetur tortor dolor in mauris. Nunc porttitor massa vel sagittis lobortis. Aenean molestie lacinia mauris non bibendum. Nullam in mi eleifend, suscipit lorem ut, luctus sapien. Mauris id sapien eu ante vestibulum viverra. Cras auctor mi at nulla dictum mollis. Quisque faucibus sem magna, ut finibus orci fringilla id. Aliquam at augue eget eros euismod viverra non non quam.</p>
        <a class="more-button" href="#">vite mer</a>
      </div>
    </section>

    <section class="service" style="top:1360px">
      <div class="service-photo photo-bulb" role="img" aria-label="En hånd holder en lyspære foran varme lys"></div>
      <div class="service-body">
        <h2 class="service-title">Kurs og workshops</h2>
        <p class="service-text">Lorem ipsum dolor sit amet, consectetur adipiscing elit. Nunc auctor, lectus in ultrices semper, sapien mi venenatis mauris, id consectetur tortor dolor in mauris. Nunc porttitor massa vel sagittis lobortis. Aenean molestie lacinia mauris non bibendum. Nullam in mi eleifend, suscipit lorem ut, luctus sapien. Mauris id sapien eu ante vestibulum viverra. Cras auctor mi at nulla dictum mollis. Quisque faucibus sem magna, ut finibus orci fringilla id. Aliquam at augue eget eros euismod viverra non non quam.</p>
        <a class="more-button" href="#">vite mer</a>
      </div>
    </section>

    <section class="service" style="top:1845px">
      <div class="service-photo photo-sky" role="img" aria-label="To hender strekker seg mot hverandre mot en skyhimmel"></div>
      <div class="service-body">
        <h2 class="service-title">Terapi og utvikling</h2>
        <p class="service-text">Lorem ipsum dolor sit amet, consectetur adipiscing elit. Nunc auctor, lectus in ultrices semper, sapien mi venenatis mauris, id consectetur tortor dolor in mauris. Nunc porttitor massa vel sagittis lobortis. Aenean molestie lacinia mauris non bibendum. Nullam in mi eleifend, suscipit lorem ut, luctus sapien. Mauris id sapien eu ante vestibulum viverra. Cras auctor mi at nulla dictum mollis. Quisque faucibus sem magna, ut finibus orci fringilla id. Aliquam at augue eget eros euismod viverra non non quam.</p>
        <a class="more-button" href="#">vite mer</a>
      </div>
    </section>
  </main>

  <footer class="site-footer">
    <p class="copyright">Copy Right 2020 @ Your Company - ETC</p>
    <div class="social">
      <span class="social-dot"></span>
      <span class="social-dot"></span>
      <span class="social-dot"></span>
    </div>
  </footer>
</div>
</body>
</html>
```